Copper Gavel Auctions business card design with existing logo

Looking for a sleek and sexy design using our current logo

Contact Information for Business Card

Name, address, email, phone, website. Gregory Vandale 482 Thornbury Road Suite 214C Marlow Falls NY 14583 Coppergavelbids.net (555)482-6613

```html
<!DOCTYPE html>
<html lang="en">
<head>
<meta charset="utf-8">
<title>Copper Gavel Auctions – Business Card</title>
<link rel="stylesheet" href="https://fonts.googleapis.com/css2?family=Roboto:wght@400;500;700;900&display=swap">
<style>
  :root {
    --bg: #2b2b2d;
    --navy: #0c3f7e;
    --red: #d0203a;
    --teal: #1fa3c6;
    --white: #ffffff;
    --ink: #1a1a1a;
    --blue-text: #1d3f8f;
  }
  * { margin: 0; padding: 0; box-sizing: border-box; }
  html, body {
    width: 1200px; height: 852px; overflow: hidden;
    background: var(--bg);
    font-family: "Roboto", Arial, sans-serif;
  }
  .stage { position: relative; width: 1200px; height: 852px; }

  .card {
    position: absolute;
    width: 520px; height: 300px;
    border-radius: 22px;
    overflow: hidden;
    box-shadow: 0 10px 24px rgba(0,0,0,.45);
  }

  /* Back side */
  .card-back { left: 110px; top: 90px; background: var(--navy); }
  .back-mark {
    position: absolute; left: 50%; top: 50%;
    transform: translate(-50%, -50%);
    display: flex; align-items: center; gap: 16px;
  }
  .back-mark .dot {
    flex: none;
    width: 64px; height: 64px; border-radius: 50%;
    background: var(--teal);
  }
  .back-mark .name {
    color: var(--teal);
    font-weight: 900; font-size: 30px;
    text-transform: uppercase; letter-spacing: .5px; line-height: 1.05;
    white-space: nowrap;
  }

  /* Front side */
  .card-front { left: 570px; top: 440px; background: var(--white); }
  .front-band { position: absolute; inset: 0; width: 520px; height: 300px; }
  .brand { position: absolute; left: 26px; top: 34px; }
  .brand .name {
    color: var(--red);
    font-weight: 900; font-size: 22px;
    text-transform: uppercase; letter-spacing: .6px;
  }
  .brand .tagline {
    margin-top: 4px;
    color: var(--blue-text);
    font-weight: 500; font-size: 15px;
    letter-spacing: 3px; text-transform: uppercase;
  }

  .front-mark {
    position: absolute; right: 24px; top: 120px;
    display: flex; align-items: center; gap: 8px;
  }
  .front-mark .dot {
    flex: none;
    width: 44px; height: 44px; border-radius: 50%;
    background: var(--white);
  }
  .front-mark .name {
    color: var(--white);
    font-weight: 900; font-size: 14px;
    text-transform: uppercase; line-height: 15px;
    white-space: nowrap;
  }

  .person { position: absolute; left: 26px; top: 150px; color: var(--white); }
  .person .full-name {
    font-weight: 900; font-size: 19px; line-height: 22px;
    text-transform: uppercase; letter-spacing: .3px;
  }
  .person .role { font-size: 11px; line-height: 14px; }
  .contacts { list-style: none; margin-top: 6px; }
  .contacts li {
    display: flex; align-items: center; gap: 9px;
    font-size: 11.5px; line-height: 16px;
  }
  .contacts svg { width: 11px; height: 11px; fill: var(--white); flex: none; }

  .address {
    position: absolute; left: 26px; bottom: 13px;
    color: var(--ink); font-size: 12px; font-weight: 500;
  }
</style>
</head>
<body>
<main class="stage">

  <section class="card card-back" aria-label="Business card back">
    <div class="back-mark">
      <span class="dot"></span>
      <span class="name">Copper Gavel<br>Auctions</span>
    </div>
  </section>

  <section class="card card-front" aria-label="Business card front">
    <svg class="front-band" viewBox="0 0 520 300" aria-hidden="true">
      <defs>
        <linearGradient id="bandGrad" x1="0" y1="1" x2="1" y2="0">
          <stop offset="0" stop-color="#1c3a8a"/>
          <stop offset=".5" stop-color="#6b2a6f"/>
          <stop offset="1" stop-color="#d0203a"/>
        </linearGradient>
      </defs>
      <polygon points="0,140 360,110 520,0 520,220 0,266" fill="url(#bandGrad)"/>
    </svg>

    <div class="brand">
      <div class="name">Copper Gavel Auctions</div>
      <div class="tagline">Buy-Sell-Consign</div>
    </div>

    <div class="front-mark">
      <span class="dot"></span>
      <span class="name">Copper<br>Gavel<br>Auctions</span>
    </div>

    <div class="person">
      <div class="full-name">Gregory Vandale</div>
      <div class="role">Managing Director</div>
      <ul class="contacts">
        <li><svg viewBox="0 0 24 24"><path d="M6.6 10.8a15 15 0 0 0 6.6 6.6l2.2-2.2a1 1 0 0 1 1-.25 11.4 11.4 0 0 0 3.6.57 1 1 0 0 1 1 1V20a1 1 0 0 1-1 1A17 17 0 0 1 3 4a1 1 0 0 1 1-1h3.5a1 1 0 0 1 1 1c0 1.25.2 2.45.57 3.57a1 1 0 0 1-.25 1z"/></svg>(555)482-6613</li>
        <li><svg viewBox="0 0 24 24"><path d="M2 5h20v14H2zm2 2v.5l8 5 8-5V7l-8 5z"/></svg>Greg@Coppergavelbids.net</li>
        <li><svg viewBox="0 0 24 24"><path d="M12 2a10 10 0 1 0 0 20 10 10 0 0 0 0-20zm0 2c.8 1.1 1.5 2.5 1.9 4h-3.8c.4-1.5 1.1-2.9 1.9-4zM4.3 14a8 8 0 0 1 0-4h3.4a16 16 0 0 0 0 4zM12 20c-.8-1.1-1.5-2.5-1.9-4h3.8c-.4 1.5-1.1 2.9-1.9 4zm2.3-6H9.7a14 14 0 0 1 0-4h4.6a14 14 0 0 1 0 4zm2 0a16 16 0 0 0 0-4h3.4a8 8 0 0 1 0 4z"/></svg>www.Coppergavelbids.net</li>
      </ul>
    </div>

    <div class="address">482 Thornbury Road Suite 214C Marlow Falls NY 14583</div>
  </section>

</main>
</body>
</html>
```